New Zealand Luggage Importer Needs Business Cards

We need professional, creative and fashionable business cards created.
We are based in New Zealand and import and distribute high-end, quality, fashionable and durable luggage.
We pride ourselves on selling the very best quality luggage, second only to 1 brand (which we won't mention here)...we use the same manufacturer. However, our prices are much more reasonable.
Industry/Entity Type
Business
Contact Information for Business Card
Mark Dunsley
027 512 4068
3/17 Harlow Street, Pinecrest Flats, Auckland, 0614
PO Box 204377, Fernside, Auckland 0731
09-528-3916
sales@brivancases.co.nz / www.brivancases.co.nz

```html
<!DOCTYPE html>
<html lang="en">
<head>
<meta charset="UTF-8">
<title>Brivan Cases – Business Cards</title>
<link href="https://fonts.googleapis.com/css2?family=Montserrat:wght@300;400;500;700;800&display=swap" rel="stylesheet">
<style>
  :root {
    --backdrop: #2b1a13;
    --card: #0a0a0a;
    --white: #ffffff;
    --text: #e9e9e9;
    --gold: #c9a54a;
    --gold-light: #f3dc8f;
    --gold-dark: #a8842c;
  }
  * { margin: 0; padding: 0; box-sizing: border-box; }
  html, body {
    width: 1200px;
    height: 1000px;
    overflow: hidden;
    background: var(--backdrop);
    font-family: "Montserrat", sans-serif;
  }
  .stage { position: relative; width: 1200px; height: 1000px; }

  .card {
    position: absolute;
    width: 525px;
    height: 300px;
    background: var(--card);
    color: var(--text);
    box-shadow: 0 10px 28px rgba(0,0,0,0.45);
  }
  .card--front { left: 145px; top: 160px; }
  .card--back  { left: 488px; top: 512px; }

  .brand-name {
    position: absolute;
    left: 0; right: 0;
    text-align: center;
    font-weight: 800;
    font-size: 38px;
    letter-spacing: 1px;
    color: var(--white);
    line-height: 1;
  }
  .card--front .brand-name { top: 112px; }
  .card--back .brand-name { top: 62px; font-size: 34px; }

  /* Front: addresses */
  .address-bar {
    position: absolute;
    left: 24px; right: 22px;
    top: 246px;
    display: flex;
    align-items: center;
    font-size: 11.5px;
    line-height: 16px;
    font-weight: 400;
  }
  .address { white-space: nowrap; }
  .address--right { text-align: right; }
  .address-rule {
    flex: 1;
    height: 1px;
    background: var(--gold);
    margin: 0 6px;
  }
  .pin-badge { width: 28px; height: 28px; flex: none; }

  /* Back */
  .person-name {
    position: absolute;
    left: 0; right: 0;
    top: 140px;
    text-align: center;
    font-size: 27px;
    color: var(--white);
    line-height: 1;
  }
  .person-name .first { font-weight: 400; }
  .person-name .last { font-weight: 700; }

  .divider {
    position: absolute;
    left: 36px; right: 34px;
    top: 212px;
    height: 2px;
    background: linear-gradient(90deg, var(--gold-dark), var(--gold-light) 50%, var(--gold-dark));
  }

  .contacts {
    position: absolute;
    top: 235px;
    display: flex;
    flex-direction: column;
    gap: 6px;
    font-size: 13.5px;
    font-weight: 400;
  }
  .contacts--left { left: 36px; }
  .contacts--right { left: 283px; }
  .contact { display: flex; align-items: center; gap: 9px; height: 17px; white-space: nowrap; }
  .contact-icon { width: 17px; height: 17px; flex: none; }
</style>
</head>
<body>
<div class="stage">
  <svg width="0" height="0" style="position:absolute">
    <defs>
      <linearGradient id="gold-fill" x1="0" y1="0" x2="0" y2="1">
        <stop offset="0" stop-color="#f6e29b"/>
        <stop offset="1" stop-color="#b48a2f"/>
      </linearGradient>
    </defs>
  </svg>

  <section class="card card--front">
    <div class="brand-name">BRIVAN CASES</div>
    <div class="address-bar">
      <div class="address address--left">PO Box 204377, Fernside<br>Auckland 0731</div>
      <div class="address-rule"></div>
      <svg class="pin-badge" viewBox="0 0 28 28">
        <circle cx="14" cy="14" r="14" fill="url(#gold-fill)"/>
        <path d="M14 7a4.8 4.8 0 0 0-4.8 4.8c0 3.6 4.8 8.7 4.8 8.7s4.8-5.1 4.8-8.7A4.8 4.8 0 0 0 14 7z" fill="#111"/>
        <circle cx="14" cy="11.8" r="1.8" fill="#d9bb62"/>
      </svg>
      <div class="address-rule"></div>
      <div class="address address--right">3/17 Harlow Street, Pinecrest Flats<br>Auckland 0614</div>
    </div>
  </section>

  <section class="card card--back">
    <div class="brand-name">BRIVAN CASES</div>
    <div class="person-name"><span class="first">MARK</span> <span class="last">DUNSLEY</span></div>
    <div class="divider"></div>

    <div class="contacts contacts--left">
      <div class="contact">
        <svg class="contact-icon" viewBox="0 0 17 17"><circle cx="8.5" cy="8.5" r="8.5" fill="url(#gold-fill)"/><path d="M4 7.5c0-1.5 2-2.5 4.5-2.5S13 6 13 7.5v.8h-2.2v-1h-4.6v1H4z M5.5 9h6l.8 3.2H4.7z" fill="#111"/></svg>
        <span>09 528 3916</span>
      </div>
      <div class="contact">
        <svg class="contact-icon" viewBox="0 0 17 17"><circle cx="8.5" cy="8.5" r="8.5" fill="url(#gold-fill)"/><path d="M4 7.5c0-1.5 2-2.5 4.5-2.5S13 6 13 7.5v.8h-2.2v-1h-4.6v1H4z M5.5 9h6l.8 3.2H4.7z" fill="#111"/></svg>
        <span>027 512 4068</span>
      </div>
    </div>

    <div class="contacts contacts--right">
      <div class="contact">
        <svg class="contact-icon" viewBox="0 0 17 17"><circle cx="8.5" cy="8.5" r="8.5" fill="url(#gold-fill)"/><g fill="none" stroke="#111" stroke-width="1"><circle cx="8.5" cy="8.5" r="4.5"/><ellipse cx="8.5" cy="8.5" rx="2" ry="4.5"/><line x1="4" y1="8.5" x2="13" y2="8.5"/></g></svg>
        <span>www.brivancases.co.nz</span>
      </div>
      <div class="contact">
        <svg class="contact-icon" viewBox="0 0 17 17"><circle cx="8.5" cy="8.5" r="8.5" fill="url(#gold-fill)"/><rect x="4.3" y="5.5" width="8.4" height="6" rx="0.6" fill="#111"/><path d="M4.6 6l3.9 3 3.9-3" fill="none" stroke="#d9bb62" stroke-width="0.8"/></svg>
        <span>sales@brivancases.co.nz</span>
      </div>
    </div>
  </section>
</div>
</body>
</html>
```